Varden Institute for Restorative Care

I need a full informational website for my medical practice. I would like to use my logo and also include a lot of emblems/pictures (also a picture of me in a white coat). The website should have a function for people to inquire and send me messages. I will be offering needle-less regenerative injection therapy, stem cell treatments, bioidentical hormone therapy, treatment for chronic illness, neurodegenerative diseases, skin rejuvenation, hair restoration, male enhancement, female enhancement, and anti-aging. The practice will not be accepting insurance and will be cash/credit card only.
A good example of written content and functionality is this website:
http://thebrvx.example/. However, I want different theme and tones.
Target Market(s)
High end clientele in Los Angeles, Southern California. Health minded people who are interested in living better and longer and can afford anti-aging treatments. Men and women who want to improve sexual health and wellbeing.
Requirements
Must have
- 1. I will need to be able to move the site to other servers (needed for site speed)
- 2. Site must be build on WordPress
- 3. Full admin credentials for domain, cpanel, wordpress, ftp.
- 4. No third party interaction on development and content deployment once the site is on different servers
- 5. I will need the ability to add content and links to the site
- 6. I will need the ability to optimize the site for speed
- 7. I will need to ability to modify URLs so they are more SEO friendly
Nice to have
- pictures of stem cells, health improvement and regeneration, beauty, youthful individuals, older healthy and happy individuals. Medical designs.
Should not have
- flowers, dna

```html
<!DOCTYPE html>
<html lang="en">
<head>
<meta charset="utf-8">
<title>Varden Institute for Restorative Care</title>
<link rel="stylesheet" href="https://fonts.googleapis.com/css2?family=Cinzel:wght@400;600&family=Open+Sans:ital,wght@0,400;0,600;1,400&display=swap">
<style>
:root{
  --navy:#1d2d6b;
  --teal:#74c6b5;
  --teal-deep:#27a79a;
  --teal-light:#9bd8ca;
  --sky:#70bfe1;
  --sky-line:#a9d9ee;
  --heading-blue:#4fb0e0;
  --green:#1fa37a;
  --text:#666;
  --footer:#e9f3f7;
  --white:#fff;
}
*{box-sizing:border-box;margin:0;padding:0}
html,body{width:1200px;height:2894px;overflow:hidden;background:var(--white)}
body{position:relative;font-family:"Open Sans",Arial,sans-serif;color:var(--text)}
.abs{position:absolute}
.serif{font-family:"Cinzel",Georgia,serif}

/* header */
.nav-band{left:0;top:114px;width:1200px;height:60px;background:linear-gradient(#94d6c8,#6fbcaa)}
.brand-notch{left:450px;top:0;width:300px;height:150px;background:var(--white);border-radius:0 0 60px 60px}
.brand{left:450px;top:70px;width:300px;text-align:center;font-family:"Cinzel",serif;font-size:46px;font-weight:600;color:var(--navy);letter-spacing:2px}
.brand-dot{left:580px;top:14px;width:40px;height:40px;border-radius:50%;background:var(--navy)}
.nav{top:132px;font-size:16px;color:var(--white);letter-spacing:.3px}
.nav.active::after{content:"";position:absolute;left:-4px;right:-4px;top:34px;height:4px;background:var(--navy)}
.enquiry{left:908px;top:44px;font-size:13px;color:var(--teal);letter-spacing:.5px}
.phone{left:848px;top:68px;font-size:20px;color:var(--navy);display:flex;align-items:center;gap:6px}

/* hero */
.hero{left:0;top:174px;width:1200px;height:620px;background:radial-gradient(circle at 30% 40%,#1f5fa8,#0b2a5e 55%,#04122c)}
.hero-title{left:0;top:388px;width:1200px;text-align:center;color:var(--white);font-family:"Cinzel",serif;font-weight:600;font-size:46px;letter-spacing:1px}
.hero-sub{left:0;top:448px;width:1200px;text-align:center;color:#e6eefc;font-size:21px;line-height:34px}
.hero-mark{left:580px;top:310px;width:40px;height:40px;border-radius:50%;background:#3aa8d8}
.slider{left:550px;top:672px;display:flex;align-items:center;gap:6px}
.slider .arrow{width:16px;height:16px;border-radius:50%;background:var(--white)}
.slider .dot{width:7px;height:7px;border-radius:50%;background:#9ab}
.slider .dot.on{background:var(--white)}

/* about */
.about-title{left:189px;top:846px;font-family:"Cinzel",serif;font-size:38px;color:var(--heading-blue)}
.about-lead{left:189px;top:916px;width:440px;font-size:15px;line-height:26px}
.about-body{left:189px;top:978px;width:440px;font-size:13px;line-height:25px}
.btn{display:flex;align-items:center;justify-content:center;color:var(--white);font-size:16px;letter-spacing:.5px}
.read-more{left:191px;top:1125px;width:160px;height:44px;background:var(--teal)}
.portrait-ring{left:655px;top:804px;width:370px;height:370px;border-radius:50%;background:var(--sky-line)}
.portrait{left:669px;top:818px;width:342px;height:342px;border-radius:50%;background:linear-gradient(135deg,#e8e9ee,#b9bcc6)}

/* services */
.services{left:0;top:1254px;width:1200px;height:526px;background:var(--sky)}
.notch{width:90px;height:45px;border-radius:0 0 45px 45px;background:var(--white);left:555px}
.notch-dot{width:30px;height:30px;border-radius:50%;left:585px}
.section-title{left:0;width:1200px;text-align:center;font-family:"Cinzel",serif;font-size:28px;color:var(--white);letter-spacing:1px}
.card{top:1364px;width:266px;height:318px;background:var(--white);border-radius:4px;box-shadow:0 2px 6px rgba(0,0,0,.15)}
.card-img{position:absolute;left:10px;top:10px;width:246px;height:150px}
.card h3{position:absolute;left:10px;right:10px;top:178px;text-align:center;font-weight:400;font-size:18px;line-height:20px;color:var(--teal-deep)}
.card p{position:absolute;left:28px;right:28px;text-align:center;font-size:12px;line-height:18px;color:#888}
.view-more{left:522px;top:1709px;width:164px;height:47px;border:2px solid var(--white)}

/* testimonial */
.video-frame{left:156px;top:1883px;width:448px;height:278px;background:#e4e4e4}
.video{left:166px;top:1893px;width:428px;height:258px;background:linear-gradient(120deg,#f1ebe4,#cbbfb3)}
.play{left:348px;top:1984px;width:64px;height:64px}
.testi-title{left:644px;top:1884px;font-family:"Cinzel",serif;font-size:28px;color:#333}
.quote{left:646px;top:1944px;width:380px;font-style:italic;font-size:14px;line-height:25px;color:#777}
.quote .mark{color:var(--teal);font-size:34px;font-style:normal;font-family:Georgia,serif;line-height:0}
.author{left:658px;top:2068px;font-size:13px;font-weight:600;color:#333}
.t-dots{left:660px;top:2110px;display:flex;gap:6px}
.t-dots span{width:10px;height:10px;border-radius:50%;background:#888}
.t-dots span.off{background:none;border:1px solid #888}

/* contact */
.contact{left:0;top:2273px;width:1200px;height:486px;background:var(--teal)}
.field{left:185px;width:461px;height:40px;border:1.5px solid var(--white);color:var(--white);font-size:13px;padding:10px 16px;opacity:.95}
.submit{left:185px;top:2641px;width:160px;height:43px;background:var(--green)}
.info-label{left:727px;font-size:16px;font-weight:600;color:var(--white);letter-spacing:.3px}
.info-value{left:727px;font-size:15px;color:var(--white)}
.socials{left:727px;top:2628px;display:flex;gap:9px}
.socials span{width:32px;height:32px;border-radius:50%;border:2px solid var(--white)}

/* footer */
.footer{left:0;top:2759px;width:1200px;height:135px;background:var(--footer)}
.foot-nav{left:0;top:2796px;width:1200px;display:flex;justify-content:center;gap:42px;font-size:16px;color:#333}
.copy{left:0;top:2833px;width:1200px;text-align:center;font-size:12px;color:#555}
</style>
</head>
<body>

<header>
  <div class="abs nav-band"></div>
  <div class="abs brand-notch"></div>
  <div class="abs brand-dot"></div>
  <div class="abs brand">Varden</div>
  <nav>
    <span class="abs nav active" style="left:185px">HOME</span>
    <span class="abs nav" style="left:262px">ABOUT US</span>
    <span class="abs nav" style="left:378px">SERVICES</span>
    <span class="abs nav" style="left:712px">TESTIMONIAL</span>
    <span class="abs nav" style="left:851px">NEWS</span>
    <span class="abs nav" style="left:929px">CONTACT</span>
  </nav>
  <div class="abs enquiry">FOR ENQUIRY</div>
  <div class="abs phone">
    <svg width="18" height="18" viewBox="0 0 24 24"><path fill="#27a79a" d="M6.6 10.8a15 15 0 0 0 6.6 6.6l2.2-2.2c.3-.3.7-.4 1-.2 1.1.4 2.3.6 3.6.6.6 0 1 .4 1 1V20c0 .6-.4 1-1 1A17 17 0 0 1 3 4c0-.6.4-1 1-1h3.5c.6 0 1 .4 1 1 0 1.3.2 2.5.6 3.6.1.3 0 .7-.2 1z"/></svg>
    (310) 555 0187
  </div>
</header>

<section>
  <div class="abs hero" role="img" aria-label="Magnified blue stem cells"></div>
  <svg class="abs" style="left:0;top:700px" width="1200" height="100" viewBox="0 0 1200 100">
    <path d="M0 92 Q600 -20 1200 92 L1200 100 L0 100Z" fill="#70bfe1"/>
    <path d="M0 100 Q600 4 1200 100Z" fill="#fff"/>
  </svg>
  <div class="abs hero-mark"></div>
  <h1 class="abs hero-title">STEM CELL TREATMENTS</h1>
  <p class="abs hero-sub">Lorem ipsum dolor sit amet consectetuer adipiscing elit Nam<br>cursus Morbi ut mi Nullam enim egestas</p>
  <div class="abs slider"><span class="arrow"></span><span class="dot on"></span><span class="dot"></span><span class="dot"></span><span class="dot"></span><span class="arrow"></span></div>
</section>

<section>
  <h2 class="abs about-title">About Varden</h2>
  <p class="abs about-lead">Morbi porta libero id ullamcorper nonummy nibh ligula pulvinar metus eget consectetuer augue nisi quis lacus</p>
  <p class="abs about-body">lacus mollis aliquam vwscelerisque mi tortor at ipsum cligula augue bibendum accumsan vestibulum ut commodo a mi Morbi ornare gravida elit Integer congue augue et malesuada iaculis ipsum dui aliquet felis at cursus magna nisl nec elit Praesent elementum elit at tellus nec ultricies sit amet porttitor mattis enim In massa libero interdum</p>
  <div class="abs btn read-more">READ MORE</div>
  <div class="abs portrait-ring"></div>
  <div class="abs portrait" role="img" aria-label="Portrait of the physician in a white coat"></div>
</section>

<section>
  <div class="abs services"></div>
  <div class="abs notch" style="top:1254px"></div>
  <div class="abs notch-dot" style="top:1240px;background:var(--navy)"></div>
  <h2 class="abs section-title" style="top:1294px">OUR SERVICES</h2>
  <svg class="abs" style="left:100px;top:1496px" width="30" height="56"><path d="M24 4 L6 28 L24 52" fill="none" stroke="#fff" stroke-width="3"/></svg>
  <svg class="abs" style="left:1070px;top:1496px" width="30" height="56"><path d="M6 4 L24 28 L6 52" fill="none" stroke="#fff" stroke-width="3"/></svg>
  <article class="abs card" style="left:185px">
    <div class="card-img" role="img" aria-label="Therapist treating a patient's shoulder" style="background:linear-gradient(135deg,#d9cfc6,#5c4a42)"></div>
    <h3>NEEDLE-LESS<br>REGENERATIVE<br>INJECTION THERAPY</h3>
    <p style="top:246px">Class aptent taciti sociosqu ad litora torquent per conubia</p>
  </article>
  <article class="abs card" style="left:467px">
    <div class="card-img" role="img" aria-label="Illustration of pink stem cells" style="background:linear-gradient(135deg,#8fd3ee,#d23b8c)"></div>
    <h3>STEM CELL<br>TREATMENTS</h3>
    <p style="top:226px">Class aptent taciti sociosqu ad litora torquent per conubia nostra per inceptos hymenaeos</p>
  </article>
  <article class="abs card" style="left:750px">
    <div class="card-img" role="img" aria-label="Hormone molecule illustration" style="background:linear-gradient(135deg,#c4558a,#b9a860)"></div>
    <h3>BIOIDENTICAL<br>HORMONE THERAPY</h3>
    <p style="top:226px">Class aptent taciti sociosqu ad litora torquent per conubia nostra per inceptos hymenaeos</p>
  </article>
  <div class="abs btn view-more">VIEW MORE</div>
</section>

<section>
  <div class="abs video-frame"></div>
  <div class="abs video" role="img" aria-label="Video of a smiling patient at home"></div>
  <svg class="abs play" viewBox="0 0 64 64"><circle cx="32" cy="32" r="32" fill="#fff"/><path d="M25 18 L47 32 L25 46Z" fill="#111"/></svg>
  <h2 class="abs testi-title">What Our Patient Says</h2>
  <p class="abs quote"><span class="mark">&ldquo;</span> Morbi porta libero id ullamcorper nonummy nibh ligula pulvinar metus eget consectetuer augue nisi quis lacus Ut ac mi quis lacus mollis aliquam vwscelerisque mi tortor at ipsum cligula augue bibendum accumsan<span class="mark">&rdquo;</span></p>
  <div class="abs author">BY AUTHOR NAME</div>
  <div class="abs t-dots"><span class="off"></span><span></span><span></span></div>
</section>

<section>
  <div class="abs contact"></div>
  <div class="abs notch" style="top:2273px"></div>
  <div class="abs notch-dot" style="top:2258px;background:var(--teal-deep)"></div>
  <h2 class="abs section-title" style="top:2318px">CONTACT US</h2>
  <div class="abs field" style="top:2392px">Name</div>
  <div class="abs field" style="top:2440px">Email address</div>
  <div class="abs field" style="top:2489px">Subject</div>
  <div class="abs field" style="top:2539px;height:86px">Message</div>
  <div class="abs btn submit">SUBMIT</div>
  <div class="abs info-label" style="top:2386px">ADDRESS</div>
  <div class="abs info-value" style="top:2412px">482 Larkmoor Avenue, Suite 3, Los Angeles CA 90025</div>
  <div class="abs info-label" style="top:2466px">PHONE</div>
  <div class="abs info-value" style="top:2492px">310.555.0142</div>
  <div class="abs info-label" style="top:2545px">EMAIL US</div>
  <div class="abs info-value" style="top:2571px">hello@varden.example</div>
  <div class="abs socials"><span></span><span></span><span></span><span></span><span></span></div>
</section>

<footer>
  <div class="abs footer"></div>
  <nav class="abs foot-nav"><span>HOME</span><span>ABOUT US</span><span>SERVICES</span><span>NEWS</span><span>TESTIMONIAL</span><span>CONTACT</span></nav>
  <p class="abs copy">© 2018 Company Name &nbsp;All right reserved &nbsp;Term of Use</p>
</footer>

</body>
</html>
```